Business Card & Stationery for Oil Company
Oil Company
Professional
Reginald P. Hawthorne
Executive Vice President
P.O. Box 584
Carlow, IL 61873
reggie@halbrenoil.com
www.halbrenoil.com

```html
<!DOCTYPE html>
<html lang="en">
<head>
<meta charset="utf-8">
<title>Halbren Oil Company – Stationery Set</title>
<link rel="stylesheet" href="https://fonts.googleapis.com/css2?family=Oswald:wght@400;700&family=Open+Sans:wght@400;600;700&display=swap">
<style>
  :root {
    --bg: #e9e6e2;
    --paper: #ffffff;
    --ink: #1e1a1a;
    --muted: #6d6666;
    --brand-red: #a3161b;
    --deep-red: #5c0b0e;
    --rule: #cfcaca;
    --faint: rgba(163, 22, 27, 0.09);
  }
  * { box-sizing: border-box; margin: 0; padding: 0; }
  html, body { width: 1200px; height: 430px; overflow: hidden; }
  body {
    background: var(--bg);
    font-family: "Open Sans", Arial, sans-serif;
    color: var(--ink);
    position: relative;
  }
  .piece { position: absolute; background: var(--paper); box-shadow: 0 2px 5px rgba(0,0,0,.25); overflow: hidden; }
  .label { position: absolute; font-size: 9px; color: #3a3434; letter-spacing: .3px; }

  /* wordmark */
  .wordmark { display: flex; align-items: center; gap: 3px; }
  .wordmark .dot { background: var(--brand-red); flex: none; }
  .wordmark .name { font-family: "Oswald", Impact, sans-serif; font-weight: 700; color: var(--ink); line-height: 1; }
  .tagline { font-size: 3px; color: var(--muted); letter-spacing: .4px; text-transform: uppercase; }

  /* business card fronts */
  .card-front .wordmark { position: absolute; left: 5px; top: 5px; }
  .card-front .wordmark .dot { width: 6px; height: 6px; }
  .card-front .wordmark .name { font-size: 7px; }
  .card-front .details { position: absolute; right: 5px; top: 15px; text-align: right; font-size: 3px; line-height: 3.8px; color: var(--muted); white-space: nowrap; }
  .card-front .details strong { color: var(--brand-red); font-size: 3.6px; display: block; line-height: 4.4px; }
  .card-front .base { position: absolute; left: 0; right: 0; bottom: 0; height: 3px; background: var(--brand-red); }

  .card-mini .wordmark { left: 3px; top: 3px; }
  .card-mini .wordmark .dot { width: 4px; height: 4px; }
  .card-mini .wordmark .name { font-size: 5px; }
  .card-mini .details { top: 12px; right: 3px; font-size: 2.4px; line-height: 3.2px; }
  .card-mini .details strong { font-size: 2.8px; line-height: 3.6px; }
  .card-mini .base { height: 2px; }

  /* business card backs */
  .card-back { display: flex; flex-direction: column; align-items: center; justify-content: center; }
  .card-back .wordmark .name { font-size: 13px; }
  .card-back .wordmark .dot { width: 10px; height: 10px; }

  /* letterhead */
  .sheet .head { position: absolute; top: 10px; left: 0; right: 0; display: flex; flex-direction: column; align-items: center; }
  .sheet .head .wordmark .dot { width: 12px; height: 12px; }
  .sheet .head .wordmark .name { font-size: 15px; }
  .sheet .foot { position: absolute; bottom: 8px; left: 0; right: 0; text-align: center; font-size: 3.2px; color: var(--muted); line-height: 4.5px; }
  .sheet .foot-rule { position: absolute; bottom: 20px; left: 20%; right: 20%; height: 1px; background: var(--brand-red); }
  .watermark {
    position: absolute; left: 0; right: 0; top: 95px; text-align: center;
    font-family: "Oswald", Impact, sans-serif; font-weight: 700; font-size: 36px; color: var(--faint);
  }

  /* fax form */
  .fax-title { position: absolute; left: 10px; top: 14px; font-family: "Oswald", Impact, sans-serif; font-size: 11px; font-weight: 700; }
  .fax-lines { position: absolute; left: 10px; right: 10px; top: 52px; font-size: 3.4px; color: var(--muted); }
  .fax-lines div { border-bottom: 1px solid var(--rule); padding: 3px 0 2px; }
  .fax-checks { position: absolute; left: 10px; right: 10px; top: 108px; display: flex; justify-content: space-between; font-size: 3.2px; color: var(--muted); }
  .fax-checks span::before { content: ""; display: inline-block; width: 3px; height: 3px; border: .5px solid var(--ink); margin-right: 1px; }

  /* folder */
  .folder-back .contact { position: absolute; left: 14px; bottom: 34px; font-size: 3.4px; color: var(--muted); line-height: 4.6px; }
  .folder-front .head { position: absolute; right: 14px; top: 12px; display: flex; flex-direction: column; align-items: center; }
  .folder-front .head .wordmark .dot { width: 12px; height: 12px; }
  .folder-front .head .wordmark .name { font-size: 16px; }
  .pocket { position: absolute; left: 0; bottom: 0; width: 100%; height: 100px; }

  /* envelope */
  .envelope .wordmark { position: absolute; left: 6px; top: 26px; }
  .envelope .wordmark .dot { width: 7px; height: 7px; }
  .envelope .wordmark .name { font-size: 9px; }
  .envelope .address { position: absolute; left: 6px; top: 40px; font-size: 3px; color: var(--muted); line-height: 4px; }
</style>
</head>
<body>

<!-- top business cards -->
<div class="piece card-front" style="left:252px;top:34px;width:66px;height:44px;">
  <div class="wordmark"><span class="dot"></span><span class="name">HALBREN</span></div>
  <div class="details"><strong>Reginald P. Hawthorne</strong>Executive Vice President<br>P.O. Box 584<br>Carlow, IL 61873<br>reggie@halbrenoil.com<br>www.halbrenoil.com</div>
  <div class="base"></div>
</div>
<div class="piece card-back" style="left:330px;top:34px;width:78px;height:44px;">
  <div class="wordmark"><span class="dot"></span><span class="name">HALBREN</span></div>
  <div class="tagline">Oil Company</div>
</div>
<div class="label" style="left:342px;top:84px;">Back 1</div>
<div class="piece card-back" style="left:420px;top:34px;width:88px;height:46px;">
  <div class="wordmark"><span class="dot"></span><span class="name">HALBREN</span></div>
  <div class="tagline">Oil Company</div>
</div>
<div class="label" style="left:455px;top:84px;">Back 2</div>

<!-- small letterhead left -->
<div class="piece sheet" style="left:12px;top:187px;width:41px;height:58px;">
  <div style="position:absolute;left:5px;top:5px;width:7px;height:7px;background:var(--brand-red)"></div>
  <div style="position:absolute;left:5px;right:5px;top:18px;height:30px;background:repeating-linear-gradient(#ddd 0 1px,transparent 1px 4px)"></div>
</div>

<!-- folder -->
<div class="label" style="left:145px;top:100px;">BACK</div>
<div class="label" style="left:326px;top:100px;">FRONT</div>
<div class="piece folder-back" style="left:125px;top:114px;width:175px;height:246px;">
  <div class="contact">Halbren Oil Company<br>P.O. Box 584, Carlow, IL 61873<br>www.halbrenoil.com</div>
</div>
<div class="piece folder-front" style="left:300px;top:114px;width:125px;height:246px;">
  <div class="head">
    <div class="wordmark"><span class="dot"></span><span class="name">HALBREN</span></div>
    <div class="tagline">Oil Company</div>
  </div>
  <svg class="pocket" viewBox="0 0 125 100" preserveAspectRatio="none" aria-hidden="true">
    <defs>
      <linearGradient id="pocketBand" x1="0" x2="1">
        <stop offset="0" stop-color="#e9d7d7"/><stop offset=".55" stop-color="#8e1216"/><stop offset="1" stop-color="#3d0608"/>
      </linearGradient>
    </defs>
    <path d="M0 22 Q62 4 125 14 L125 100 L0 100 Z" fill="#f6f1f1"/>
    <rect x="0" y="62" width="125" height="38" fill="url(#pocketBand)"/>
    <path d="M0 22 Q62 4 125 14" fill="none" stroke="#b7a9a9" stroke-width=".6"/>
  </svg>
  <div class="piece card-front card-mini" style="left:60px;top:198px;width:58px;height:32px;box-shadow:0 1px 3px rgba(0,0,0,.4)">
    <div class="wordmark"><span class="dot"></span><span class="name">HALBREN</span></div>
    <div class="details"><strong>Reginald P. Hawthorne</strong>reggie@halbrenoil.com</div>
    <div class="base"></div>
  </div>
</div>

<!-- letterhead option 1 -->
<div class="piece sheet" style="left:440px;top:115px;width:190px;height:233px;">
  <div class="head"><div class="wordmark"><span class="dot"></span><span class="name">HALBREN</span></div><div class="tagline">Oil Company</div></div>
  <div class="foot-rule"></div>
  <div class="foot">P.O. Box 584 · Carlow, IL 61873 · Tel 618.555.0142<br>reggie@halbrenoil.com · www.halbrenoil.com</div>
</div>
<div class="label" style="left:510px;top:352px;">Option-1</div>

<!-- letterhead option 2 -->
<div class="piece sheet" style="left:660px;top:115px;width:185px;height:233px;">
  <div class="head"><div class="wordmark"><span class="dot"></span><span class="name">HALBREN</span></div><div class="tagline">Oil Company</div></div>
  <div class="watermark">HALBREN</div>
  <div class="foot-rule"></div>
  <div class="foot">P.O. Box 584 · Carlow, IL 61873 · Tel 618.555.0142<br>reggie@halbrenoil.com · www.halbrenoil.com</div>
</div>
<div class="label" style="left:730px;top:352px;">Option-2</div>

<!-- fax option 3 -->
<div class="piece sheet" style="left:865px;top:115px;width:190px;height:233px;">
  <div class="fax-title">FAX</div>
  <div class="wordmark" style="position:absolute;right:10px;top:12px;"><span class="dot" style="width:8px;height:8px"></span><span class="name" style="font-size:10px">HALBREN</span></div>
  <div class="fax-lines">
    <div>To:</div><div>From:</div><div>Fax:</div><div>Date:</div><div>Pages:</div>
  </div>
  <div class="fax-checks"><span>Urgent</span><span>For Review</span><span>Please Comment</span><span>Please Reply</span></div>
  <div class="foot-rule"></div>
  <div class="foot">P.O. Box 584 · Carlow, IL 61873 · Fax 618.555.0143</div>
</div>
<div class="label" style="left:935px;top:352px;">Option 3</div>

<!-- envelope -->
<div class="piece envelope" style="left:1075px;top:175px;width:115px;height:77px;">
  <svg style="position:absolute;left:0;top:0" width="115" height="22" viewBox="0 0 115 22" aria-hidden="true">
    <path d="M0 0 L115 0 L115 6 Q58 22 0 6 Z" fill="var(--deep-red)"/>
  </svg>
  <div class="wordmark"><span class="dot"></span><span class="name">HALBREN</span></div>
  <div class="address">P.O. Box 584<br>Carlow, IL 61873</div>
</div>

<!-- small cards right -->
<div class="piece card-front card-mini" style="left:1068px;top:262px;width:60px;height:30px;">
  <div class="wordmark"><span class="dot"></span><span class="name">HALBREN</span></div>
  <div class="details"><strong>Reginald P. Hawthorne</strong>Executive Vice President</div>
  <div class="base"></div>
</div>
<div class="piece card-front card-mini" style="left:1130px;top:262px;width:60px;height:30px;">
  <div class="wordmark"><span class="dot"></span><span class="name">HALBREN</span></div>
  <div class="details"><strong>Reginald P. Hawthorne</strong>www.halbrenoil.com</div>
  <div class="base"></div>
</div>

<!-- bottom card backs -->
<div class="piece card-back" style="left:980px;top:355px;width:88px;height:44px;">
  <div class="wordmark"><span class="dot"></span><span class="name">HALBREN</span></div>
  <div class="tagline">Oil Company</div>
</div>
<div class="label" style="left:1008px;top:404px;">Back 1</div>
<div class="piece card-back" style="left:1082px;top:355px;width:106px;height:44px;">
  <div class="wordmark"><span class="dot"></span><span class="name">HALBREN</span></div>
  <div class="tagline">Oil Company</div>
</div>
<div class="label" style="left:1120px;top:404px;">Back 2</div>

</body>
</html>
```